Visitenkarten-Design für Goldankauf und Verkauf von Trauringen
Zielgruppe
Goldankauf und Verkauf von Trauringen
Aufgabenstellung
Edel, nicht zu bunt, das Design soll sich dem Kunden einprägen, ansprechend, gerne können auch Wasserzeichen verwendet werden.

```html
<!DOCTYPE html>
<html lang="de">
<head>
<meta charset="utf-8">
<title>Glanzstunde – Visitenkarten</title>
<link href="https://fonts.googleapis.com/css2?family=Cormorant+Garamond:wght@500&family=Libre+Baskerville&display=swap" rel="stylesheet">
<style>
  :root {
    --page-bg: #efefef;
    --card-black: #111111;
    --card-black-soft: #1d1d1d;
    --gold-dark: #a8801f;
    --gold: #d9b23c;
    --gold-light: #f4dd7a;
    --text-light: #e9e6df;
  }
  * { margin: 0; padding: 0; box-sizing: border-box; }
  html, body { width: 1200px; height: 3000px; overflow: hidden; }
  body {
    background: var(--page-bg);
    position: relative;
    font-family: "Libre Baskerville", serif;
  }
  .card {
    position: absolute;
    left: 100px;
    width: 1000px;
    height: 606px;
    background: radial-gradient(ellipse at 40% 35%, var(--card-black-soft), var(--card-black) 75%);
    box-shadow: 0 14px 30px rgba(0,0,0,0.18);
    overflow: hidden;
  }
  .card::before, .card::after {
    content: "";
    position: absolute;
    top: 0;
    width: 16px;
    height: 100%;
    background: linear-gradient(180deg, var(--gold-dark), var(--gold-light) 45%, var(--gold) 60%, var(--gold-dark));
  }
  .card::before { left: 0; }
  .card::after { right: 0; }

  .card--front { top: 820px; }
  .brand {
    position: absolute;
    left: 50%;
    top: 50%;
    transform: translate(-50%, -50%);
    display: flex;
    align-items: center;
    gap: 22px;
  }
  .brand__mark {
    width: 34px;
    height: 34px;
    border-radius: 50%;
    background: var(--gold);
  }
  .brand__name {
    font-family: "Cormorant Garamond", serif;
    font-weight: 500;
    font-size: 84px;
    color: var(--gold);
    letter-spacing: 2px;
  }

  .card--contact { top: 1620px; }
  .owner {
    position: absolute;
    left: 120px;
    top: 90px;
    font-family: "Cormorant Garamond", serif;
    font-weight: 500;
    font-size: 58px;
    line-height: 1;
    color: var(--gold);
    text-transform: uppercase;
    letter-spacing: 1px;
  }
  .owner-details {
    position: absolute;
    left: 120px;
    top: 222px;
    font-size: 21px;
    line-height: 1.45;
    color: var(--text-light);
  }
  .address {
    position: absolute;
    left: 120px;
    bottom: 80px;
    font-size: 23px;
    line-height: 1.5;
    color: var(--text-light);
  }
</style>
</head>
<body>
  <section class="card card--front" aria-label="Vorderseite">
    <div class="brand">
      <span class="brand__mark"></span>
      <span class="brand__name">Glanzstunde</span>
    </div>
  </section>

  <section class="card card--contact" aria-label="Rückseite">
    <h1 class="owner">Inh. Marena<br>Holzbrück</h1>
    <p class="owner-details">
      info@glanzstunde-altenfurt.de<br>
      Mobil: 06100-4471201
    </p>
    <p class="address">
      Lindenhof-Gasse 12 • 63450 Altenfurt<br>
      Tel.: 06100-4471201 • Fax: 06100-4471202<br>
      www.glanzstunde-altenfurt.de<br>
      info@glanzstunde-altenfurt.de
    </p>
  </section>
</body>
</html>
```